Stationery Design for Family Law Firm
BROOK VESTAL, LLP
Stationery Design for Family Law Firm -
Creative Brief
Professional
Martin D. Vestal
Attorney & Counselor at Law
4187 Larkin Street San Diego, CA 92104
martin@brookvestal-law.example
www.brookvestal-law.example
Paper will be ivory. Please use large and small caps for name and "Attorney & Counselor" at Law. Sentence case for the rest.
Family Law I Guardianships I Conservatorships I Estate Planning

```html
<!DOCTYPE html>
<html lang="en">
<head>
<meta charset="utf-8">
<title>Brook Vestal, LLP — Business Cards</title>
<link href="https://fonts.googleapis.com/css2?family=EB+Garamond:wght@500&family=Arimo:wght@400;700&display=swap" rel="stylesheet">
<style>
  :root{
    --bg:#e9e6df;
    --ivory:#fbfaf6;
    --ivory-edge:#e3e1da;
    --ink:#1f2a36;
    --ink-soft:#4a525b;
    --blue:#1f8fd0;
    --blue-light:#4fb0e6;
    --black-card:#0c0d0f;
    --black-card-top:#23262a;
    --on-dark:#e8eaec;
    --on-dark-soft:#a9adb2;
  }
  *{box-sizing:border-box;margin:0;padding:0}
  html,body{width:1200px;height:914px;overflow:hidden}
  body{background:var(--bg);font-family:"Arimo",Arial,sans-serif;position:relative}
  .card-sheet{
    position:absolute;left:80px;top:151px;
    display:grid;grid-template-columns:500px 500px;grid-template-rows:286px 286px;gap:40px;
  }
  .card{position:relative;border-radius:14px;overflow:hidden;box-shadow:0 2px 6px rgba(0,0,0,.12)}
  .card--ivory{background:var(--ivory);border:1px solid var(--ivory-edge);color:var(--ink)}
  .card--dark{background:linear-gradient(180deg,var(--black-card-top) 0%,var(--black-card) 55%);color:var(--on-dark)}

  .firm-mark{display:flex;align-items:center;gap:10px}
  .firm-mark__square{width:16px;height:16px;background:var(--blue)}
  .firm-mark__name{font-family:"EB Garamond",Georgia,serif;font-weight:500;font-size:30px;letter-spacing:.02em;line-height:1}
  .card--ivory .firm-mark__name{color:var(--ink)}
  .card--dark .firm-mark__name{color:var(--on-dark)}
  .firm-tagline{font-family:"EB Garamond",Georgia,serif;font-variant:small-caps;font-size:15px;letter-spacing:.04em;margin-top:6px;padding-left:26px}

  /* front */
  .card--front .firm-block{position:absolute;left:34px;top:36px}
  .accent-bar{position:absolute;left:0;top:142px;width:10px;height:66px;background:var(--blue)}
  .contact{position:absolute;left:34px;top:146px;font-size:11px;line-height:15px}
  .card--ivory .contact{color:var(--ink-soft)}
  .card--dark .contact{color:var(--on-dark-soft)}
  .person{position:absolute;left:258px;top:160px}
  .person__name{font-variant:small-caps;font-weight:700;font-size:15px;color:var(--blue)}
  .person__title{font-variant:small-caps;font-size:11px;margin-top:2px}
  .card--dark .person__title{color:var(--on-dark-soft)}
  .web{position:absolute;left:34px;bottom:26px;font-size:11px;color:var(--blue)}

  /* back */
  .card--back .firm-block{position:absolute;left:0;right:0;top:78px;display:flex;flex-direction:column;align-items:center}
  .card--back .firm-tagline{padding-left:26px}
  .practice-areas{position:absolute;left:0;right:0;top:184px;text-align:center;font-size:13.5px;color:var(--blue)}
  .card--dark .practice-areas{color:var(--blue-light)}
  .rule{position:absolute;left:24px;right:24px;top:208px;height:1px;background:var(--blue);opacity:.6}
  .card--back .web{left:0;right:0;text-align:center;bottom:36px}
  .card--ivory.card--back .web{color:var(--ink-soft)}
  .card--dark.card--back .web{color:var(--blue-light)}
</style>
</head>
<body>
  <main class="card-sheet">
    <section class="card card--ivory card--front">
      <div class="firm-block">
        <div class="firm-mark"><span class="firm-mark__square"></span><span class="firm-mark__name">BROOK VESTAL, LLP</span></div>
        <div class="firm-tagline">Attorneys &amp; Counselors at Law</div>
      </div>
      <div class="accent-bar"></div>
      <div class="contact">4187 Larkin Street<br>San Diego, CA 92104<br>Phone: (619) 555-0142<br>Email: martin@brookvestal-law.example</div>
      <div class="person"><div class="person__name">Martin D. Vestal</div><div class="person__title">Attorney &amp; Counselor at Law</div></div>
      <div class="web">www.brookvestal-law.example</div>
    </section>

    <section class="card card--dark card--front">
      <div class="firm-block">
        <div class="firm-mark"><span class="firm-mark__square"></span><span class="firm-mark__name">BROOK VESTAL, LLP</span></div>
        <div class="firm-tagline">Attorneys &amp; Counselors at Law</div>
      </div>
      <div class="accent-bar"></div>
      <div class="contact">4187 Larkin Street<br>San Diego, CA 92104<br>Phone: (619) 555-0142<br>Email: martin@brookvestal-law.example</div>
      <div class="person"><div class="person__name">Martin D. Vestal</div><div class="person__title">Attorney &amp; Counselor at Law</div></div>
      <div class="web">www.brookvestal-law.example</div>
    </section>

    <section class="card card--ivory card--back">
      <div class="firm-block">
        <div class="firm-mark"><span class="firm-mark__square"></span><span class="firm-mark__name">BROOK VESTAL, LLP</span></div>
        <div class="firm-tagline">Attorneys &amp; Counselors at Law</div>
      </div>
      <div class="practice-areas">Family Law | Guardianships | Conservatorships | Estate Planning</div>
      <div class="web">www.brookvestal-law.example</div>
    </section>

    <section class="card card--dark card--back">
      <div class="firm-block">
        <div class="firm-mark"><span class="firm-mark__square"></span><span class="firm-mark__name">BROOK VESTAL, LLP</span></div>
        <div class="firm-tagline">Attorneys &amp; Counselors at Law</div>
      </div>
      <div class="practice-areas">Family Law | Guardianships | Conservatorships | Estate Planning</div>
      <div class="rule"></div>
      <div class="web">www.brookvestal-law.example</div>
    </section>
  </main>
</body>
</html>
```